Website visual upgrade

I am seeking expressions of interest for the updating the visuals of my website www.lunvaleplacements.example
I am basically seeking a simple,bold and visually strong graphic makeover.using existing or shortly to be modified text.

```html
<!DOCTYPE html>
<html lang="en">
<head>
<meta charset="utf-8">
<title>Lunvale Placements</title>
<link href="https://fonts.googleapis.com/css2?family=Open+Sans:ital,wght@0,400;0,600;1,700&display=swap" rel="stylesheet">
<style>
:root{
  --charcoal:#3a3a3c;
  --panel:#3b3b3d;
  --red:#c41e2f;
  --white:#ffffff;
  --ink:#1e1e1e;
  --btn-top:#fafafa;
  --btn-bottom:#cfcfcf;
}
*{box-sizing:border-box;margin:0;padding:0}
html,body{width:1200px;height:1048px;overflow:hidden;background:var(--white);font-family:"Open Sans",sans-serif}
.page{position:relative;width:1200px;height:1048px}
.topbar{position:absolute;left:0;top:0;width:1200px;height:47px;background:var(--charcoal);border-bottom:2px solid var(--red)}
.social{position:absolute;right:148px;top:13px;display:flex;gap:14px;align-items:center}
.social span{display:block;width:20px;height:20px;border-radius:50%;background:#6d6d70}
.social svg{display:block}
.brand{position:absolute;left:156px;top:80px;display:flex;align-items:center;gap:10px}
.brand-dot{width:18px;height:18px;border-radius:50%;background:var(--ink)}
.brand-name{font-size:24px;font-weight:600;color:var(--red);letter-spacing:.3px}
.nav{position:absolute;left:463px;top:48px;height:111px;display:flex}
.nav a{display:flex;align-items:center;padding:0 15px;font-size:15.5px;color:var(--ink);text-decoration:none}
.nav a.active{background:var(--red);color:var(--white);width:74px;justify-content:center;padding:0}
.slider{position:absolute;left:145px;top:159px;width:908px;height:422px;background:linear-gradient(180deg,#9fd0f3 0%,#cfe7f8 45%,#8ea9a7 68%,#5d7d45 80%,#2f6fb3 92%,#2459a0 100%)}
.arrow{position:absolute;top:190px;width:35px;height:40px;background:var(--charcoal);display:flex;align-items:center;justify-content:center}
.arrow.prev{left:1px}.arrow.next{right:0}
.pager{position:absolute;right:0;bottom:0;display:flex;gap:2px}
.pager span{width:21px;height:21px;display:flex;align-items:center;justify-content:center;font-size:14px;font-weight:600;background:var(--charcoal);color:var(--white)}
.pager span.on{background:var(--white);color:var(--ink)}
.card{position:absolute;top:586px;width:300px;height:382px}
.card h2{height:34px;background:var(--red);border-radius:6px 6px 0 0;color:var(--white);font-size:20px;font-weight:700;font-style:italic;padding:3px 18px;line-height:28px}
.card .photo{margin-top:6px;height:135px}
.card .body{height:207px;background:var(--panel);border-radius:0 0 8px 8px;padding:12px 20px 0 23px;position:relative}
.card p{color:var(--white);font-size:12.3px;line-height:22.4px}
.more{position:absolute;right:23px;bottom:18px;width:88px;height:25px;border:1px solid #999;background:linear-gradient(var(--btn-top),var(--btn-bottom));font-size:10.5px;color:#333;display:flex;align-items:center;justify-content:center}
.footer{position:absolute;left:0;top:988px;width:1200px;height:46px;background:var(--charcoal);color:var(--white);font-size:19px;font-weight:600;display:flex;align-items:center;justify-content:center}
</style>
</head>
<body>
<div class="page">
  <header class="topbar">
    <div class="social">
      <svg width="24" height="18" viewBox="0 0 24 18"><rect x="1" y="2" width="22" height="14" rx="2" fill="none" stroke="#6d6d70" stroke-width="2.5"/><path d="M2 3l10 8 10-8" fill="none" stroke="#6d6d70" stroke-width="2.5"/></svg>
      <span></span><span></span><span></span><span></span>
    </div>
  </header>

  <div class="brand"><div class="brand-dot"></div><div class="brand-name">Lunvale Placements</div></div>

  <nav class="nav">
    <a class="active" href="#">Home</a>
    <a href="#">Who we are</a>
    <a href="#">Job seeker</a>
    <a href="#">Useful links</a>
    <a href="#">Support</a>
    <a href="#">Contact us</a>
  </nav>

  <section class="slider" role="img" aria-label="City skyline with towers beside a river under a blue sky">
    <div class="arrow prev"><svg width="12" height="22" viewBox="0 0 12 22"><path d="M10 2L2 11l8 9" fill="none" stroke="#fff" stroke-width="2"/></svg></div>
    <div class="arrow next"><svg width="12" height="22" viewBox="0 0 12 22"><path d="M2 2l8 9-8 9" fill="none" stroke="#fff" stroke-width="2"/></svg></div>
    <div class="pager"><span>1</span><span class="on">2</span><span>3</span></div>
  </section>

  <article class="card" style="left:142px">
    <h2>Our Approach</h2>
    <div class="photo" role="img" aria-label="Red combine harvester in a wheat field" style="background:linear-gradient(180deg,#c9ccd0 0%,#aeb2b6 45%,#b89a68 60%,#9c7f52 100%)"></div>
    <div class="body">
      <p>We think laterally about our clients’ needs and deliver a “fresh approach” to Executive search and selection and the provision of Skilled trades people and allied Health recruitment. This fresh approach results in a clear advantage to our clients.</p>
      <div class="more">Read more</div>
    </div>
  </article>

  <article class="card" style="left:450px">
    <h2>What we do</h2>
    <div class="photo" role="img" aria-label="Three health sector staff standing together in an office" style="background:linear-gradient(90deg,#e4e4e2 0%,#d9d4cf 40%,#5c7a4e 55%,#4a2f30 80%,#dcdcda 100%)"></div>
    <div class="body">
      <p>We are a specialist recruiter to the Health sector. Our clienes andts are primarily engaged in the management of acute hospitals, residential aged care facilities, community care servic other health related services. We are recruitment specialists in the following areas:</p>
      <div class="more">Read more</div>
    </div>
  </article>

  <article class="card" style="left:757px">
    <h2>Migration assistance</h2>
    <div class="photo" role="img" aria-label="A family standing together in a recruitment office" style="background:linear-gradient(180deg,#6f5a45 0%,#3a2e26 45%,#2a2624 75%,#6c6866 100%)"></div>
    <div class="body">
      <p>We can provide processing assistance to employers who are seeking suitably skilled and experienced staff from overseas on an appropriate temporary/permanent business visa.</p>
      <div class="more">Read more</div>
    </div>
  </article>

  <footer class="footer">Copyright © 2013 www.lunvaleplacements.example, All rights reserved.</footer>
</div>
</body>
</html>
```